Seeking a business card and logo for a blockchain technology and strategy expert who is looking to expand their personal brand. Dave is looking to gain consulting roles and bring attention to upcoming blogging and podcasts with this card. For the business card, prefer two-sided but open to any shape or size, even if non-standard. Color scheme is open to the designer but preference for light blue (#70BFEA) complimenting black (#000500). This is a blockchain project, but designs don’t need to be limited to the standard blockchain-esque work. For visual reference, Dave’s favorite logo is the Pogo caricature for The Wayfarers.Minimum information on the card should include email (Dave@LedgerDave.example) and phone number (provided later). The ideal card would be 1) playful but professional, 2) visually reference that it is for a blockchain expert, and 3) stand-out from other cards. Will consider incorporating technology elements (NFC, QR codes, private/public keys) on either the front or back of the card.Dave has been active in Bitcoin/blockchain since 2011, and built blockchain technology practices at Fortune 100 companies, Unicorn-exit startups, and advised successful ICOs. Dave recently returned to independent consulting and has begun creating social content, such as podcasts, blogs, and conference panels.
Target Market(s)
Blockchain companies and those looking to expand into the space.
People interested in the technology and looking for expert sources.
Industry/Entity Type
Blockchain
Contact Information for Business Card
For the business card, prefer two-sided but open to any shape or size, even if non-standard. Color scheme is open to the designer but preference for light blue (#70BFEA) complimenting black (#000500). This is a blockchain project, but designs don’t need to be limited to the standard blockchain-esque work. For visual reference, Dave’s favorite logo is the Pogo caricature for The Wayfarers.
Minimum information on the card should include email (Dave@LedgerDave.example) and phone number (provided later).
The ideal card would be 1) playful but professional, 2) visually reference that it is for a blockchain expert, and 3) stand-out from other cards. Will consider incorporating technology elements (NFC, QR codes, private/public keys) on either the front or back of the card.
Colors
Designer to choose colors to be used in the design.

```html
<!DOCTYPE html>
<html lang="en">
<head>
<meta charset="utf-8">
<title>Ledger Dave – Business Card</title>
<link rel="stylesheet" href="https://fonts.googleapis.com/css2?family=Roboto:wght@400;500&family=Exo+2:wght@800&display=swap">
<style>
  :root {
    --stage: #a3a3a3;
    --card-dark: #0b0d0c;
    --card-light: #ffffff;
    --brand-blue: #3f56b5;
    --ink: #1f1f1f;
    --white: #ffffff;
  }
  * { box-sizing: border-box; margin: 0; padding: 0; }
  html, body { width: 1200px; height: 930px; overflow: hidden; }
  body {
    background: var(--stage);
    font-family: "Roboto", Arial, sans-serif;
    position: relative;
  }
  .card {
    position: absolute;
    width: 560px;
    height: 320px;
    border-radius: 26px;
    box-shadow: 0 8px 18px rgba(0,0,0,0.25);
  }
  .card--back {
    left: 80px; top: 90px;
    background: var(--card-dark);
    display: flex; align-items: center; justify-content: center;
  }
  .card--front {
    left: 560px; top: 500px;
    background: var(--card-light);
  }
  .wordmark {
    display: flex; align-items: center; gap: 12px;
    font-family: "Exo 2", "Arial Black", sans-serif;
    font-weight: 800;
    letter-spacing: 2px;
    text-transform: uppercase;
  }
  .wordmark__square {
    width: 34px; height: 34px;
    background: var(--brand-blue);
  }
  .card--back .wordmark { font-size: 40px; color: var(--white); }
  .card--front .wordmark {
    position: absolute; right: 44px; top: 44px;
    font-size: 30px; color: var(--ink);
  }
  .card--front .wordmark__square { width: 26px; height: 26px; }
  .rule-main {
    position: absolute; left: 40px; right: 40px; top: 172px;
    height: 1.5px; background: var(--brand-blue);
  }
  .person__name {
    position: absolute; left: 40px; top: 136px;
    font-size: 27px; font-weight: 500; letter-spacing: 1px;
    color: var(--brand-blue); text-transform: uppercase;
  }
  .person__role {
    position: absolute; left: 40px; top: 182px;
    font-size: 15px; color: var(--ink);
  }
  .address {
    position: absolute; right: 40px; top: 118px;
    text-align: right; font-size: 15px; line-height: 1.45; color: var(--ink);
  }
  .rule-short {
    position: absolute; left: 40px; top: 214px;
    width: 190px; height: 1.5px; background: var(--brand-blue);
  }
  .contacts {
    position: absolute; left: 60px; top: 228px;
    list-style: none; font-size: 15px; color: var(--ink);
  }
  .contacts li { display: flex; align-items: center; gap: 8px; height: 23px; }
  .contacts svg { width: 11px; height: 11px; fill: none; stroke: var(--brand-blue); stroke-width: 1.6; }
  .contacts .accent { color: var(--brand-blue); }
</style>
</head>
<body>

<section class="card card--back" aria-label="Card back">
  <div class="wordmark"><span class="wordmark__square"></span>Ledger Dave</div>
</section>

<section class="card card--front" aria-label="Card front">
  <div class="wordmark"><span class="wordmark__square"></span>Ledger Dave</div>

  <p class="address">48b Ferris Lane,<br>Norwood, NZ, 7020</p>
  <h1 class="person__name">Dave Harlow</h1>
  <div class="rule-main"></div>
  <p class="person__role">Director</p>
  <div class="rule-short"></div>

  <ul class="contacts">
    <li>
      <svg viewBox="0 0 12 12"><path d="M2 1.5 L4 1.5 L5 4 L3.8 5 Q5 7.5 7 8.2 L8 7 L10.5 8 L10.5 10 Q5 10.5 2 4 Z"/></svg>
      (555) 010-2741
    </li>
    <li>
      <svg viewBox="0 0 12 12"><rect x="1" y="2.5" width="10" height="7"/><path d="M1 2.5 L6 6.5 L11 2.5"/></svg>
      info@ledgerdave.example
    </li>
    <li>
      <svg viewBox="0 0 12 12"><circle cx="6" cy="6" r="5"/><ellipse cx="6" cy="6" rx="2.2" ry="5"/><path d="M1 6 H11"/></svg>
      www.<span class="accent">ledgerdave</span>.example
    </li>
  </ul>
</section>

</body>
</html>
```